High-End Medical Center Website Design Project

This design is part of a well thought-out project by an experienced project manager / developer. The approved wireframe is attached. Creative interpretations / suggestions based on the layout encouraged.

The design is for a new state-of-the-art medical center located in Dallas, Texas. The target audience would likely be individuals (approx. 60% female /40% male) who are the healthcare decision-makers for their families. They would likely have insurance and be inclined to seek out top-quality care.

Potential clients would choose this client over others in their industry because the medical center is physician owned, meaning it is patient-focused rather than profit-focused. The facility is brand new, featuring the latest technology. (This includes an amazing waiting room featuring WiFi and docking stations.) The physicians are hand-picked by referral only.

The look of the site should be extremely clean. We are going for a well-organized, professional look with a bit of a warm glow (interpret that however you like). Use crisp corners and the colors in the logo.

Think modern, clean with some great use of color / font.

We can get lovely photography of the medical center once construction is complete. Feel free to use an "example image" behind the Featured Area ("Physician Owned. Patient-Focused") if you like. We are open to ideas.

ONE CHANGE REQUESTED IN THE WIREFRAME:

Remove the "Connect" 1/4 page footer area and replace with a quick contact form. You may swap the "Locations" area with the form if desired. Put social media icons at the top left of the page in the top header area.

(Note: Please use social media icons that match the design rather than standard icons. We preferred not placing the icons at the top, but the client requested this. Let's not bring more attention to them than necessary.)
Updates

We're custom programming this site, so there's no need to base it on a template. Also, we would prefer not to use typical "seen everywhere" stock images.Thanks.

Industry/Entity Type

Construction

Requirements
Must have
• Follow the wireframe. This has been approved.
Nice to have
• Examples of what hover states, links or dropdowns might look like.

```html
<!DOCTYPE html>
<html lang="en">
<head>
<meta charset="utf-8">
<title>APEX Medical Center</title>
<link href="https://fonts.googleapis.com/css2?family=Open+Sans:ital,wght@0,300;0,400;0,600;0,700;1,400;1,600;1,700&display=swap" rel="stylesheet">
<style>
:root{
  --blue:#0b56a5;
  --band:#1a68b8;
  --teal:#45adb8;
  --teal-dark:#3a9da8;
  --teal-light:#5fd3e0;
  --ink:#555;
  --grey-bg:#f3f3f3;
  --white:#fff;
}
*{margin:0;padding:0;box-sizing:border-box}
html,body{width:990px;height:1200px;overflow:hidden;background:#fff}
body{font-family:'Open Sans',Arial,sans-serif;color:var(--ink)}
.page{position:relative;width:990px;height:1200px}
.abs{position:absolute}

/* top bar */
.topbar{left:0;top:0;width:990px;height:24px;background:var(--blue)}
.social{top:6px;width:14px;height:14px;border:1px solid #8fb8e0}
.social.active{background:var(--teal);border-color:var(--teal)}
.callnow{right:178px;top:5px;font-size:10px;color:#fff}

/* header */
.logo{left:178px;top:42px;display:flex;align-items:center;gap:6px}
.logo-mark{width:22px;height:22px;background:var(--teal)}
.logo-name{font-size:19px;font-weight:700;color:var(--blue);letter-spacing:.3px}
.nav{top:24px;left:446px;height:63px;display:flex;align-items:center;font-size:9.5px;color:var(--ink)}
.nav-item{padding:0 9px;border-left:1px solid #bbb;line-height:10px}
.nav-item:first-child{border-left:0}
.nav-active{left:686px;top:24px;width:66px;height:63px;background:var(--blue);color:#fff;padding:26px 0 0 11px;font-size:9.5px;line-height:11px}
.nav-active small{display:block;font-size:7px}
.nav-last{left:761px;top:52px;font-size:9.5px}
.dropdown{left:686px;top:87px;width:126px;background:var(--blue);padding:5px 0}
.dropdown div{height:22px;line-height:22px;padding-left:13px;font-size:9.5px;color:#fff}
.dropdown .hover{background:var(--teal)}

/* hero */
.hero{left:0;top:87px;width:990px;height:250px;background:linear-gradient(100deg,#d8d2c4 0%,#e9e2d2 30%,#c9d3e0 60%,#aebfd6 100%)}
.dots{top:318px;left:469px;display:flex;gap:5px}
.dots i{width:6px;height:6px;border-radius:50%;background:var(--teal-light)}
.dots i:first-child{background:#fff;border:1px solid var(--teal-light)}
.band{left:0;top:337px;width:990px;height:192px;background:linear-gradient(180deg,#1a68b8,#2a78c4)}
.tagline{left:259px;top:387px;width:473px;height:40px;background:var(--teal);color:#fff;font-size:23px;font-weight:700;text-align:center;line-height:40px;letter-spacing:.3px}
.lead{left:270px;top:436px;width:450px;text-align:center;color:#fff;font-style:italic;font-weight:600;font-size:12.5px;line-height:16px}
.diamond{top:492px;width:77px;height:77px}

/* feature cards */
.card{top:601px;height:104px;overflow:hidden}
.card-photo{width:100%;height:100%}
.card-label{position:absolute;left:0;right:0;top:50px;text-align:center;color:#fff;font-size:9.5px;font-weight:600}
.card-label span{background:rgba(69,173,184,.85);padding:1px 7px}
.apart{position:absolute;left:0;right:0;top:38px;text-align:center;color:#fff;line-height:19px}
.apart .a1{font-size:16px;font-weight:300}
.apart .a2{font-size:20px;font-weight:700}
.card-text{background:var(--teal);color:#fff;text-align:center;padding:6px 10px}
.card-text h3{font-size:9.5px;font-weight:600;display:flex;align-items:center;gap:5px;margin-bottom:10px}
.card-text h3::before,.card-text h3::after{content:"";flex:1;border-top:3px double rgba(255,255,255,.5)}
.card-text p{font-size:8.5px;line-height:12px}

/* about + testimonials */
.grey{left:0;top:741px;width:990px;height:193px;background:radial-gradient(ellipse at 50% 100%,#fff 0%,var(--grey-bg) 60%);border-top:1px solid #e5e5e5}
.sec-title{font-size:12px;font-weight:600;color:var(--blue);display:flex;align-items:center;gap:9px}
.sec-title::after{content:"";flex:1;border-top:3px double #dcdcdc}
.about-photo{left:178px;top:787px;width:155px;height:102px;background:linear-gradient(120deg,#e4e7ea,#c8ccd0 60%,#dfe2e4)}
.about-text{left:343px;top:788px;width:245px;font-size:8px;line-height:12px;color:#666}
.btn-more{left:505px;top:880px;width:80px;height:21px;background:var(--blue);color:#fff;font-size:9.5px;line-height:21px;padding-left:9px}
.btn-more b{position:absolute;right:8px;top:5px;width:10px;height:10px;background:#fff;color:var(--blue);font-size:10px;line-height:10px;text-align:center}
.arrow-btn{width:14px;height:14px;background:var(--blue)}
.arrow-btn.alt{background:var(--teal)}
.quote-mark{left:615px;top:786px;font-size:24px;color:var(--teal);font-style:italic;font-weight:700}
.quote{left:636px;top:793px;width:170px;font-size:8.8px;line-height:13px;font-style:italic;color:#666}
.author{right:222px;top:870px;text-align:right;font-size:9.5px;color:var(--teal);line-height:11px}
.author small{display:block;font-size:7.5px;color:#555}
.avatar{left:773px;top:863px;width:38px;height:38px;border-radius:50%;border:2px solid var(--teal);background:radial-gradient(circle,#c9c2b8,#6a6560)}

/* footer */
.footer{left:0;top:934px;width:990px;height:207px;background:var(--teal)}
.f-title{font-size:11.5px;font-weight:600;color:#fff;display:flex;align-items:center;gap:8px}
.f-title.line::after{content:"";flex:1;border-top:3px double rgba(255,255,255,.35)}
.f-arrow{width:13px;height:13px;border:1px solid #fff;background:rgba(255,255,255,.25)}
.news-item{left:178px;width:137px;font-size:8.5px;line-height:10.5px;color:#fff;padding-bottom:8px;border-bottom:1px solid rgba(255,255,255,.35)}
.news-item em,.blog-item em{font-style:normal;color:var(--teal-light)}
.news-item strong{color:var(--teal-light);font-weight:600}
.blog-thumb{width:46px;height:46px;background:linear-gradient(160deg,#eef0f2,#9aa3ad);border:2px solid #fff}
.blog-item{left:385px;width:95px;font-size:8.5px;line-height:10.5px;color:#fff}
.form-label{left:496px;font-size:8.5px;color:#fff}
.field{left:545px;width:91px;background:var(--teal-dark)}
.submit{left:574px;top:1090px;width:62px;height:20px;background:var(--teal-dark);color:#fff;font-size:9.5px;font-weight:600;text-align:center;line-height:20px}
.wait{left:654px;top:952px;width:158px;height:157px;background:var(--teal-dark);padding:7px}
.wait-inner{width:100%;height:100%;border:1px dashed rgba(255,255,255,.5);text-align:center;color:#fff;padding-top:9px}
.wait-inner h4{font-size:11px;font-weight:600}
.digits{display:flex;justify-content:center;align-items:center;gap:2px;margin-top:10px}
.digit{width:22px;height:27px;background:var(--teal);font-size:23px;line-height:27px;color:#fff;border-top:1px solid rgba(255,255,255,.3)}
.colon{font-size:20px;width:6px}
.units{display:flex;justify-content:space-around;font-size:8px;margin:4px 10px 0}
.wait-inner p{font-size:8px;line-height:10px;margin:14px 10px 0}
.bottombar{left:0;top:1141px;width:990px;height:59px;background:var(--blue);font-size:8.5px;color:var(--teal-light)}
.copy{left:178px;top:16px}
.links{right:180px;top:16px}
</style>
</head>
<body>
<div class="page">

  <!-- top bar -->
  <div class="abs topbar">
    <span class="abs social active" style="left:178px"></span>
    <span class="abs social" style="left:197px"></span>
    <span class="abs social" style="left:216px"></span>
    <span class="abs callnow">Call Now : (555) 010-2048</span>
  </div>

  <!-- header -->
  <div class="abs logo"><span class="logo-mark"></span><span class="logo-name">APEX MEDICAL CENTER</span></div>
  <nav class="abs nav">
    <span class="nav-item">WHY APEX</span>
    <span class="nav-item">PHYSICIAN</span>
    <span class="nav-item">SPECIALITES</span>
    <span class="nav-item">INFO</span>
  </nav>
  <div class="abs nav-active">LOCATION<small>Where we are</small></div>
  <div class="abs nav-last">CONTAT US</div>

  <!-- hero -->
  <div class="abs hero" role="img" aria-label="Photo of a doctor with a clipboard talking with a patient"></div>
  <div class="abs band" role="img" aria-label="Blue-toned continuation of the consultation photo"></div>
  <div class="abs dots"><i></i><i></i><i></i><i></i><i></i></div>

  <div class="abs dropdown">
    <div>LOCATION -1</div>
    <div class="hover">LOCATION-2</div>
    <div>LOCATION-3</div>
  </div>

  <div class="abs tagline">PHYSICIAN OWNED. PATIENT-FOCUSED</div>
  <p class="abs lead">Lorem Ipsum is simply dummy text of the printing and typesetting industry. Lorem Ipsum has been the industry's standard dummy text..</p>

  <svg class="abs diamond" style="left:358px" viewBox="0 0 77 77">
    <rect x="16" y="16" width="45" height="45" transform="rotate(45 38.5 38.5)" fill="#0b56a5" stroke="#fff" stroke-width="1.5"/>
    <path d="M28 28v10a7 7 0 0 0 14 0V28M35 45v4a6 6 0 0 0 12 0v-9" fill="none" stroke="#fff" stroke-width="2.2"/>
    <circle cx="47" cy="37" r="2.5" fill="none" stroke="#fff" stroke-width="1.8"/>
  </svg>
  <svg class="abs diamond" style="left:457px" viewBox="0 0 77 77">
    <rect x="16" y="16" width="45" height="45" transform="rotate(45 38.5 38.5)" fill="#45adb8"/>
    <rect x="25" y="26" width="28" height="24" fill="none" stroke="#fff" stroke-width="2"/>
    <rect x="29" y="30" width="8" height="7" fill="#fff"/>
    <path d="M40 31h9M40 35h9M29 40h20M29 44h20" stroke="#fff" stroke-width="1.6"/>
  </svg>
  <svg class="abs diamond" style="left:555px" viewBox="0 0 77 77">
    <rect x="16" y="16" width="45" height="45" transform="rotate(45 38.5 38.5)" fill="#45adb8"/>
    <text x="38.5" y="49" text-anchor="middle" font-family="Open Sans, sans-serif" font-weight="700" font-size="30" fill="#fff">?</text>
  </svg>

  <!-- feature cards -->
  <div class="abs card" style="left:178px;width:173px">
    <div class="card-photo" role="img" aria-label="Photo of a surgical team in scrubs and caps" style="background:linear-gradient(160deg,#7f9cb3,#4f6f8c 60%,#7b95a8)"></div>
    <div class="apart"><div class="a1">WHAT SETS US</div><div class="a2">APART</div></div>
  </div>
  <div class="abs card card-text" style="left:364px;width:141px">
    <h3>TECHNOLOGY</h3>
    <p>Lorem Ipsum is simply dummy text of the printing and typesetting industry. Lorem Ipsum has been the industry's</p>
  </div>
  <div class="abs card" style="left:518px;width:140px">
    <div class="card-photo" role="img" aria-label="Photo of lab samples being examined" style="background:linear-gradient(135deg,#cfe3ea,#f3f6f7 50%,#e6d9a8)"></div>
    <div class="card-label"><span>QUALITY OF CORE</span></div>
  </div>
  <div class="abs card" style="left:671px;width:141px">
    <div class="card-photo" role="img" aria-label="Photo of a laser treatment in a clinic" style="background:linear-gradient(135deg,#e8eef2,#c9d6de 50%,#d8c7b6)"></div>
    <div class="card-label"><span>TECHNOLOGY</span></div>
  </div>

  <!-- about + testimonials -->
  <div class="abs grey"></div>
  <div class="abs sec-title" style="left:178px;top:766px;width:430px">APEX MEDICAL CENTER</div>
  <div class="abs about-photo" role="img" aria-label="Photo of a doctor examining a patient"></div>
  <p class="abs about-text">Lorem Ipsum is simply dummy text of the printing and typesetting industry. Lorem Ipsum has been the industry's standard dummy text ever since the 1500s, when an unknown printer took a galley of type and scrambled it to make a type specimen book. It has survived not only five centuries, but also the leap into electronic typesetting, remaining essentially unchanged. It was popularised in the 1960s.</p>
  <div class="abs btn-more">Read More<b>+</b></div>

  <div class="abs sec-title" style="left:617px;top:766px;width:158px">TESTIMONIALS</div>
  <svg class="abs arrow-btn" style="left:781px;top:767px" viewBox="0 0 14 14"><path d="M8.5 3.5 5 7l3.5 3.5" fill="none" stroke="#fff" stroke-width="1.5"/></svg>
  <svg class="abs arrow-btn alt" style="left:799px;top:767px" viewBox="0 0 14 14"><path d="M5.5 3.5 9 7l-3.5 3.5" fill="none" stroke="#fff" stroke-width="1.5"/></svg>
  <div class="abs quote-mark">&ldquo;</div>
  <p class="abs quote">Lorem Ipsum is simply dummy text look of the printing and typesetting industry. simpl Lorem Ipsum has been the industry's standard &nbsp;of the dummy text ever since the when Ipsum</p>
  <div class="abs author">Rohan Mehta<small>Police officer</small></div>
  <div class="abs avatar" role="img" aria-label="Portrait photo of the reviewer"></div>

  <!-- footer -->
  <div class="abs footer"></div>
  <div class="abs f-title" style="left:177px;top:966px">NEWS</div>
  <svg class="abs f-arrow" style="left:286px;top:967px" viewBox="0 0 13 13"><path d="M8 3 4.5 6.5 8 10" fill="none" stroke="#fff" stroke-width="1.4"/></svg>
  <svg class="abs f-arrow" style="left:303px;top:967px" viewBox="0 0 13 13"><path d="M5 3l3.5 3.5L5 10" fill="none" stroke="#fff" stroke-width="1.4"/></svg>
  <div class="abs news-item" style="top:989px"><strong>22-7-2013:</strong> <em>Lorem Ipsum is dummy text</em> : of the printing and typesetting industry. has been</div>
  <div class="abs news-item" style="top:1035px"><strong>22-7-2013:</strong> <em>Lorem Ipsum is simdummy text</em> : of the printing and typesetting industry.</div>
  <div class="abs news-item" style="top:1084px;border:0"><strong>22-7-2013:</strong> <em>Lorem Ipsum</em> is simply dummy text : of the</div>

  <div class="abs f-title line" style="left:331px;top:966px;width:149px">BLOG</div>
  <div class="abs blog-thumb" style="left:331px;top:991px" role="img" aria-label="Photo of a businessman at a laptop"></div>
  <div class="abs blog-item" style="top:993px"><em>Lorem Ipsum is simply dummy text</em> of the printing and typesetting industry.</div>
  <div class="abs" style="left:385px;top:1051px;width:95px;border-top:1px solid rgba(255,255,255,.35)"></div>
  <div class="abs blog-thumb" style="left:331px;top:1063px" role="img" aria-label="Photo of a businessman at a laptop"></div>
  <div class="abs blog-item" style="top:1066px"><em>Lorem Ipsum is simply dummy text</em> of the printing and typesetting industry.</div>

  <div class="abs f-title line" style="left:496px;top:966px;width:140px">QUICK CONTACT</div>
  <div class="abs form-label" style="top:994px">Name</div><div class="abs form-label" style="left:540px;top:994px">:</div>
  <div class="abs field" style="top:993px;height:14px"></div>
  <div class="abs form-label" style="top:1013px">Email</div><div class="abs form-label" style="left:540px;top:1013px">:</div>
  <div class="abs field" style="top:1012px;height:14px"></div>
  <div class="abs form-label" style="top:1032px">Comment</div><div class="abs form-label" style="left:540px;top:1032px">:</div>
  <div class="abs field" style="top:1031px;height:53px"></div>
  <div class="abs submit">SUBMIT</div>

  <div class="abs wait">
    <div class="wait-inner">
      <h4>AVRAGE WAIT TIME</h4>
      <div class="digits"><span class="digit">1</span><span class="digit">3</span><span class="colon">:</span><span class="digit">0</span><span class="digit">9</span></div>
      <div class="units"><span>HOUR</span><span>MINUTES</span></div>
      <p>printing and typesetting industry. has been the industry's standard dummy text ever since the</p>
    </div>
  </div>

  <div class="abs bottombar">
    <span class="abs copy">Copyright © 2013 Allright Reserved</span>
    <span class="abs links">Sitemap &nbsp;| &nbsp;Privacy policy</span>
  </div>
</div>
</body>
</html>
```